Decorative concrete business needs new business cards

Our company attracts homeowners and business with disposable cash. We are a artistic decorative coatings company that will transform your driveway, patio, floors or counter tops into a work of art. We also engrave logos and designs right into the concrete! We are upscale and very professional company. I am open for rearranging our logo on the business card and also to different color patterns. We like the blue and black as in BrushNest's logo. We also like blue and orange/yellow.

Target Market(s)

Adults 30-70

Industry/Entity Type

Concrete

Contact Information for Business Card

Simple: Name, phone, email, website and social media icons

Font styles to use
Serif

Colors

Designer to choose colors to be used in the design.

Requirements
Must have
• Must present a professional upscale appearance. I have attached before and after photos that show you what our industry does. Maybe I will have before and after photo on back of card.
Nice to have
• Artistic, but bold. Nothing whimsical or cute.
Should not have
• Should not have cartoon or childlike appearance.

```html
<!DOCTYPE html>
<html lang="en">
<head>
<meta charset="utf-8">
<title>Crafted Surface Finishes – Business Card</title>
<link rel="stylesheet" href="https://fonts.googleapis.com/css2?family=Cinzel:wght@400;600&family=Marcellus&family=Open+Sans:wght@400&display=swap">
<style>
  :root {
    --page-bg: #e6e6e6;
    --card-white: #ffffff;
    --brand-blue: #1f8bc0;
    --brand-dark: #2b2b2b;
    --text-grey: #4a4a4a;
    --rule-grey: #c9c9c9;
    --on-blue: #ffffff;
  }
  * { margin: 0; padding: 0; box-sizing: border-box; }
  html, body {
    width: 1200px; height: 987px; overflow: hidden;
    background: var(--page-bg);
  }
  .card {
    position: absolute;
    width: 615px; height: 352px;
  }
  /* Front */
  .card-front { left: 293px; top: 130px; background: var(--card-white); }
  .social-links { position: absolute; top: 17px; right: 18px; display: flex; gap: 4px; }
  .social-dot { width: 24px; height: 24px; border-radius: 50%; background: var(--brand-blue); }
  .company-mark { position: absolute; left: 62px; top: 150px; display: flex; align-items: center; gap: 12px; }
  .mark-square { width: 40px; height: 40px; background: var(--brand-blue); }
  .company-name {
    font-family: "Marcellus", serif; font-size: 25px; line-height: 1.05;
    color: var(--brand-blue); letter-spacing: 1px; text-transform: uppercase;
  }
  .divider { position: absolute; left: 330px; top: 117px; width: 1px; height: 143px; background: var(--rule-grey); }
  .contact-block { position: absolute; left: 355px; top: 117px; }
  .person-name {
    font-family: "Cinzel", serif; font-weight: 600; font-size: 25px;
    color: var(--brand-blue); letter-spacing: 1px; line-height: 30px;
  }
  .person-title {
    font-family: "Cinzel", serif; font-weight: 600; font-size: 18px;
    color: var(--brand-dark); letter-spacing: 1px; line-height: 24px; margin-bottom: 10px;
  }
  .contact-line {
    display: flex; align-items: center; gap: 9px;
    font-family: "Open Sans", sans-serif; font-size: 15.5px; color: var(--text-grey); line-height: 23.5px;
  }
  .contact-line svg { width: 14px; height: 14px; fill: var(--brand-blue); flex: none; }
  .rule-dark { position: absolute; left: 0; right: 0; bottom: 25px; height: 2px; background: var(--brand-dark); }
  .band-blue { position: absolute; left: 0; right: 0; bottom: 0; height: 23px; background: var(--brand-blue); }
  /* Back */
  .card-back {
    left: 292px; top: 505px; background: var(--brand-blue);
    display: flex; flex-direction: column; align-items: center; justify-content: center;
    color: var(--on-blue); font-family: "Marcellus", serif; text-transform: uppercase; text-align: center;
  }
  .back-name { line-height: 1; }
  .back-line-1 { font-size: 52px; letter-spacing: 1px; }
  .back-line-2 { font-size: 36px; letter-spacing: 0.5px; margin-top: 2px; }
  .back-line-3 { font-size: 30px; letter-spacing: 9px; margin-top: 2px; }
  .back-web { font-family: "Open Sans", sans-serif; text-transform: none; font-size: 16px; letter-spacing: 4px; margin-top: 10px; }
</style>
</head>
<body>
  <section class="card card-front">
    <div class="social-links">
      <span class="social-dot"></span><span class="social-dot"></span><span class="social-dot"></span><span class="social-dot"></span>
    </div>
    <div class="company-mark">
      <span class="mark-square"></span>
      <p class="company-name">Crafted<br>Surface<br>Finishes</p>
    </div>
    <div class="divider"></div>
    <div class="contact-block">
      <h1 class="person-name">Mark Ellison</h1>
      <p class="person-title">CEO/Founder</p>
      <p class="contact-line">
        <svg viewBox="0 0 24 24"><path d="M6.6 10.8a15.1 15.1 0 0 0 6.6 6.6l2.2-2.2c.3-.3.7-.4 1-.2 1.1.4 2.3.6 3.6.6.6 0 1 .4 1 1V20c0 .6-.4 1-1 1C10.6 21 3 13.4 3 4c0-.6.4-1 1-1h3.5c.6 0 1 .4 1 1 0 1.3.2 2.5.6 3.6.1.3 0 .7-.2 1z"/></svg>
        555 014 2290
      </p>
      <p class="contact-line">
        <svg viewBox="0 0 24 24"><path d="M2 5h20v14H2z M4 7v.5l8 5 8-5V7l-8 5z" fill-rule="evenodd"/></svg>
        hello@craftedsurface.com
      </p>
      <p class="contact-line">
        <svg viewBox="0 0 24 24"><circle cx="12" cy="12" r="10"/></svg>
        www.craftedsurface.com
      </p>
    </div>
    <div class="rule-dark"></div>
    <div class="band-blue"></div>
  </section>

  <section class="card card-back">
    <p class="back-name back-line-1">Crafted</p>
    <p class="back-name back-line-2">Surface</p>
    <p class="back-name back-line-3">Finishes</p>
    <p class="back-web">www.craftedsurface.com</p>
  </section>
</body>
</html>
```